Digital Imaging Website Design Project

This project is for 3 page designs - The main Home page design, department page design & content page design which will utilize most of the home page components.

Client Background - http://www.kelvarprint.example

An almost Forty year old established printing company that has a large client base of architect/engineering, as the print shop opened up as a blueprinting company, and over the years has grown, changed and expanded to offer document and digital file management for this industry. KPRInc. has also always offered color printing services, but recently has expanded their color department to be able to offer amazing dimensional printing, and extreme cutting technology.

These new products and services will be targeted to new industries for repeatable printing needs, promotional, point of purchase color printing, as well as in-store, interior decor/wall. These new printing services are only offered by KPRINC in their area, and they want to convey that they are on the leading edge of color printing technology, while at the same time, not eliminating their existing primary business scaring away their traditional client base of architectural/engineering firms that use them for large format printing, scanning and document management services.

1 - Home Page Design
Primary Goals of the design:

1.Provide a new, eye catching engaging website that conveys the above expansion/growth/cutting edge company.
2.Full screen design please to move away from the 'center' bordered up website they currently have.
3.Design Components – We don't have any media to provide you with exception of our logo. We're looking for fresh design that is exciting and engaging imagery. Additionally, we are working on a color/effected version of our logo to place on the color division page, and this will probably tie in with the design you create for us.
4.It should be designed to be able to work as a responsive design as well so that when installed, will work across devices etc..
5.Colors – Same color scheme, but if you have an accent color you'd like to use to make the site pop, go for it!

Requirements:
1.The 4 divisions of the company should be the main feature so that the client depending on which department they are needing, will see those 4 choices clearly in the design, and they'll know to click on one of them to get more information and to their needed services.

2.The main goal of the site is to get visitors to place an order, there should be a feature on the home page for this call to action.

3.Put in an element that communicates the main benefit of KPRInc. - an area for a 1-line Statement/Call to Action / Overall Company Benefit/

4.The 4 divisions need to have eye catching elements related to their products and services, and that clearly illustrate that the user should click on that to go to the appropriate area for products and services

Reprographics
This department is specifically geared to architect/engineering industry
BYLine for optional Use: Partnering with Building Industry Providers since 1975
Related pages for better understanding:
http://www.kelvarprint.example/services/portland_professional_printing_services
http://www.kelvarprint.example/services/reprographics
Digital File Management
This department is related to Architect/engineers, but can also apply to any other industry needing electronic document management, scanning, or archival services.
BYLine for optional use: Effective & Efficient Digital Solutions at every level.
Related Pages:
http://www.kelvarprint.example/colorgraphics/electronic_file_document_management
http://www.kelvarprint.example/colorgraphics/document_scanning_service
http://www.kelvarprint.example/services/scanning_and_archiving

Color Graphics
This Department is newly expanded / has expanded services / they are focusing more of their efforts on this department and is a key reason for updated website design.
This Department image/representation should be stellar in the imagery to convey the excellence of the color department the services availble.
One of their newest products/services is dimensional printing – not 3-D, but raised element printing. Essentially a client could pick components on their graphic that that they want to 'bump' out, and additional layers would be put in place to create a popped out, dimensional effect. * Bonus points for creating the color department image that effectively conveys this new service – whether it's showing an abstract image/element that is actually raised off the page/paper/component. Additionally the color dimensional printing can be done on practically any material – glass, vinyl, material etc.... Please let me know if you have any questions on this.
BYLine for optional Use: See How Our Color Stands Out From the Rest
Related pages:
http://www.kelvarprint.example/colorgraphics
http://www.kelvarprint.example/colorgraphics/color_digital_imaging

Equipment & Supplies
This department provides specific supplies and hardware vs. printing products/services. Our largest client base is architects/engineers, but is not limited to this industry. Typical equipment is large printers, and supplies are typically paper products geared to the large format printing services, for the architect/engineers industry.
Byline for optional Use: In-House Printing & Fulfillment Services
Related pages:
http://www.kelvarprint.example/tervik_amlo_equipment_sales
http://www.kelvarprint.example/supplies

Additionally - Possibly have descriptive text sections below these 4 elements, but this is optional.

2.) Department/Division Page design -

This page should pull the home page element to over based on which division is selected.
Have a submenu design incorporated so that users can navigate to all the products and services that will be listed under that division
Contain a plugin design for FAQs – so that depending on which division page they are on, the appropriate FAQ's would display for use to have easy access to.
Contain a plugin design for – Contact Us easy form – short form –
Name
Company
Number
Email
Project Details/Questions: Text box

3.)Content Page design
This page should have main area for content
Area for an image with slideshow of other supporting images
Optional area for video – most (99%) of the pages will not have videos, but in the case we do, would like an area that will display videos effectively.
Optional FAQ plugin display
Contact plugin display

Global Elements:

Static and very visible site features that are in a position so that if user clicks beyond home page will still see these are:
Get a Quote
Place Order
Digital Plan-room
Call Today - 541-867-2290

Other global components:
SM Icons – QX, Chirply, ProNexa
Rotating Testimonial

Navigational Menu:
The KPR Difference
About
Sustainability
Products & Services
Reprograhics
Digital File Management
Color Graphics
Equipment & Supplies
Login
Blog
Contact Us

After the contest – What would be great to have is when a user clicks on one of the departments, it takes that visual element and continues onto it's department page for a smaller but related image - But this may be an after this web design contest.

Additionally will need some other design work on the interior pages, as well, so hoping to find a great designer to complete the other tasks – as well as be the go-to for future endeavors!

Thanks for looking at the project, and I look forward to any questions you may have.

Looking forward to hearing from interested designers! - If you're curious about my work, you can find my profile at:  https://www.freelanzo.example/users/~07b3e2c91f4d6a05

Please see description

```html
<!DOCTYPE html>
<html lang="en">
<head>
<meta charset="utf-8">
<title>KPR Digital Imaging</title>
<link href="https://fonts.googleapis.com/css2?family=Titillium+Web:wght@400;600;700&display=swap" rel="stylesheet">
<style>
:root{
  --brand:#454a9a;
  --brand-deep:#2e3275;
  --nav-bg:#ececec;
  --hero-bg:#f6f6f6;
  --ink:#333;
  --muted:#9a9a9a;
  --accent:#2cc0d5;
  --orange:#f7901e;
  --red:#e8444a;
  --quote-red:#c8141c;
  --white:#fff;
}
*{margin:0;padding:0;box-sizing:border-box}
html,body{width:878px;height:1200px;overflow:hidden}
body{font-family:"Titillium Web",sans-serif;color:var(--ink);background:var(--white);position:relative}
.abs{position:absolute}
a{color:inherit;text-decoration:none}

/* header */
.site-header{left:0;top:0;width:878px;height:87px;background:var(--brand)}
.brand{left:132px;top:24px;display:flex;align-items:center;gap:10px;color:var(--white)}
.brand-mark{font-size:36px;font-weight:700;line-height:1}
.brand-name{font-size:10px;font-weight:700;line-height:11px;text-transform:uppercase}
.brand-name small{display:block;font-weight:400;font-size:7px;margin-top:3px;text-transform:none}
.header-copy{left:206px;top:15px;font-size:8px;color:var(--white)}
.top-links{right:132px;top:6px;display:flex;gap:10px;font-size:8px;color:var(--white)}
.order-pill{left:571px;top:50px;width:182px;height:26px;border-radius:13px;background:linear-gradient(#fff,#dfeff8);display:flex;align-items:center;justify-content:center;gap:8px;font-size:12px;font-weight:600;color:var(--ink)}

/* nav */
.main-nav{left:0;top:87px;width:878px;height:37px;background:var(--nav-bg);border-bottom:1px solid #ddd;display:flex;align-items:center;justify-content:center;gap:7px;font-size:10px;color:var(--brand)}
.main-nav .sep{color:#888}

/* hero */
.hero{left:0;top:124px;width:878px;height:240px;background:var(--hero-bg)}
.hero-visual{left:116px;top:28px;width:320px;height:190px;border-radius:50% 50% 40% 40%;background:linear-gradient(120deg,#cfd8e0 0%,#7fc4ea 30%,#f2e14a 55%,#e8412d 75%,#c8c8c8 100%);opacity:.85}
.hero-title{right:128px;top:52px;font-size:29px;font-weight:700;color:var(--brand);letter-spacing:-.5px}
.hero-lead{right:128px;top:90px;width:300px;text-align:right;font-size:10.5px;line-height:14px;color:#555}
.hero-text{right:128px;top:124px;width:300px;text-align:right;font-size:8.2px;line-height:13.5px;color:var(--muted)}
.btn-read{left:662px;top:176px;width:84px;height:28px;background:var(--orange);color:var(--white);font-size:11px;font-weight:600;display:flex;align-items:center;justify-content:center}

/* divisions */
.division{top:396px;width:145px}
.division-head{height:43px;background:var(--brand);display:flex;align-items:center;color:var(--white)}
.division-head svg{width:52px;height:43px;flex:none}
.division-head h3{font-size:11px;font-weight:600;line-height:13px;padding-left:8px}
.division p{margin-top:9px;font-size:8.2px;line-height:11.5px;color:var(--muted)}

/* quote */
.rule{left:0;width:878px;height:1px;background:#ddd}
.testimonial{left:0;top:520px;width:878px;text-align:center}
.testimonial .ask{font-size:9.5px;color:#555;text-transform:uppercase}
.testimonial .claim{font-size:17px;color:#444;text-transform:uppercase;line-height:20px}
.testimonial .q{color:var(--brand);font-weight:700;font-size:17px}
.testimonial .who{font-size:10.5px;font-weight:700;color:var(--quote-red);margin-top:4px;text-transform:uppercase}

/* portfolio */
.section-title{left:126px;top:616px;font-size:14px;font-weight:600;color:#111}
.thumb{top:648px;width:145px;height:123px}

/* info columns */
.info{top:824px;width:195px}
.info h4{font-size:11px;font-weight:600;color:#222;display:flex;align-items:center;gap:7px;text-transform:uppercase}
.info h4::before{content:"";width:10px;height:10px;background:var(--brand)}
.info p{margin-top:6px;font-size:8.2px;line-height:12.5px;color:var(--muted)}
.info p a{color:var(--accent)}
.info .news-title{color:#555;font-weight:600;display:block}
.info .news + .news{margin-top:6px}

/* footer */
.site-footer{left:0;top:962px;width:878px;height:200px;background:var(--brand);color:var(--white)}
.foot-col{top:22px}
.foot-col h5{font-size:12.5px;font-weight:400;text-transform:uppercase}
.foot-line{margin-top:6px;height:2px;background:#6a6fb2;position:relative}
.foot-line::before{content:"";position:absolute;left:0;top:0;width:30px;height:2px;background:var(--accent)}
.foot-col ul{list-style:none;margin-top:18px;font-size:8.4px;line-height:15px}
.field{left:435px;width:138px;background:#f2f2f2;border-radius:2px;font-size:7.5px;color:#888;padding:2px 8px}
.submit{left:435px;top:147px;width:47px;height:16px;background:var(--accent);font-size:8px;display:flex;align-items:center;justify-content:center;border:1px solid #1aa;}
.cta{left:600px;width:153px;height:38px;background:var(--red);display:flex;align-items:center;justify-content:center;gap:8px;font-size:14.5px;font-weight:600;color:var(--white);letter-spacing:-.3px}
.footer-base{left:0;top:1162px;width:878px;height:38px;background:var(--brand-deep);color:var(--white);font-size:8.4px;display:flex;align-items:center;justify-content:center}
</style>
</head>
<body>

<header class="site-header abs">
  <div class="header-copy abs">Copyright 2013 KPR. All Rights Reserved.</div>
  <div class="brand abs">
    <span class="brand-mark">KPR</span>
    <span class="brand-name">Kelvar<br>Print &amp; Repro<br>Company, Inc.<small>Client-Driven Service Since 1975</small></span>
  </div>
  <nav class="top-links abs"><a>Login</a><a>Blog</a><a>Contact Us</a><a>About Us</a></nav>
  <a class="order-pill abs"><span>Order Now</span><span>1-800-555-0142</span></a>
</header>

<nav class="main-nav abs">
  <a>The KPR Difference</a><span class="sep">:</span>
  <a>Sustainability</a><span class="sep">:</span>
  <a>Products &amp; Services</a><span class="sep">:</span>
  <a>Reprographics</a><span class="sep">:</span>
  <a>Digital File Management</a><span class="sep">:</span>
  <a>Color Graphics</a><span class="sep">:</span>
  <a>Equipment &amp; Supplies</a>
</nav>

<section class="hero abs">
  <div class="hero-visual abs" role="img" aria-label="Fanned colour swatch guide"></div>
  <h1 class="hero-title abs">Lorem Ipsum simplement</h1>
  <p class="hero-lead abs">Lorem Ipsum est simplement du faux texte employé dans la sition et la misen page avant impression</p>
  <p class="hero-text abs">Lorem Ipsum est simplement du faux texte employé dans la sition et la misen avant impression. Le Lorem Ipsum est le faux texte standard de l'imprimerie depuis les années 1500, quand un peintre anonyme assembla.</p>
  <a class="btn-read abs">Read More</a>
</section>

<article class="division abs" style="left:126px">
  <div class="division-head">
    <svg viewBox="0 0 52 43" aria-hidden="true"><g fill="none" stroke="#fff" stroke-width="3"><rect x="6" y="4" width="9" height="36" rx="4"/><rect x="20" y="4" width="9" height="36" rx="4"/><rect x="34" y="4" width="9" height="36" rx="4"/></g></svg>
    <h3>Graphic Imaging<br>Services</h3>
  </div>
  <p>Dolore eu feugiat nulla facilisis at vero eros et accumsan iusto odio dsim qui blandit praesent.</p>
</article>
<article class="division abs" style="left:287px">
  <div class="division-head">
    <svg viewBox="0 0 52 43" aria-hidden="true"><circle cx="26" cy="21.5" r="17" fill="none" stroke="#fff" stroke-width="4"/><circle cx="26" cy="21.5" r="8" fill="#fff"/></svg>
    <h3>Lastest Digital<br>Technology</h3>
  </div>
  <p>Dolore eu feugiat nulla facilisis at vero eros et accumsan iusto odio dsim qui blandit praesent.</p>
</article>
<article class="division abs" style="left:447px">
  <div class="division-head">
    <svg viewBox="0 0 52 43" aria-hidden="true"><circle cx="26" cy="21.5" r="19" fill="#fff"/><g fill="#454a9a"><circle cx="26" cy="10" r="4.5"/><circle cx="15" cy="24" r="4.5"/><circle cx="37" cy="24" r="4.5"/><circle cx="26" cy="33" r="3.5"/></g></svg>
    <h3>Digital Film<br>Management</h3>
  </div>
  <p>Dolore eu feugiat nulla facilisis at vero eros et accumsan iusto odio dsim qui blandit praesent.</p>
</article>
<article class="division abs" style="left:607px">
  <div class="division-head">
    <svg viewBox="0 0 52 43" aria-hidden="true"><rect x="3" y="3" width="46" height="37" fill="#fff"/><rect x="10" y="8" width="30" height="26" fill="none" stroke="#454a9a" stroke-width="1.5" stroke-dasharray="3 2"/><rect x="17" y="16" width="16" height="9" fill="none" stroke="#454a9a" stroke-width="1.5"/></svg>
    <h3>Reprographics<br>Service</h3>
  </div>
  <p>Dolore eu feugiat nulla facilisis at vero eros et accumsan iusto odio dsim qui blandit praesent.</p>
</article>

<div class="rule abs" style="top:506px"></div>
<section class="testimonial abs">
  <p class="ask"><span class="q">"</span> Cras vulputate pretium massa gravida egestas consectetur?</p>
  <p class="claim">Lorem ipsum dolor sit amet &amp; consectetur adipiscing elit! <span class="q">"</span></p>
  <p class="who">Marten Okafor</p>
</section>
<div class="rule abs" style="top:582px"></div>

<h2 class="section-title abs">PORTFOLIO</h2>
<div class="thumb abs" style="left:126px;background:linear-gradient(135deg,#dce6ef,#a9bccd)" role="img" aria-label="Rolled blueprints"></div>
<div class="thumb abs" style="left:287px;background:linear-gradient(135deg,#f2c431,#e8413b 35%,#3c8fd8 65%,#6cc04a)" role="img" aria-label="Colour swatch fan close-up"></div>
<div class="thumb abs" style="left:447px;background:linear-gradient(135deg,#f3e6c8,#e84a86 40%,#3cb8e6 70%,#222)" role="img" aria-label="Printed patterned vinyl samples"></div>
<div class="thumb abs" style="left:609px;background:linear-gradient(135deg,#b9a78a,#4a3e33 55%,#1d2233)" role="img" aria-label="Bound printed books"></div>

<section class="info abs" style="left:126px">
  <h4>Welcome to KPR</h4>
  <p>Dolore eu feugiat nulla facilisis at vero eros et accumsan et iusto odio dignissim qui blandit prae-sent luptatum zzril delenit augue duis dolore te feugait nulla facilisi. Nam liber tempor cum soluta nobis eleifend option congue nihil imperdiet doming id quod mazim placerat facer possim assum. <a>Read More</a></p>
</section>
<section class="info abs" style="left:346px">
  <h4>Equipment for sale</h4>
  <p>Dolore eu feugiat nulla facilisis at vero eros et accumsan et iusto odio dignissim qui blandit prae-sent luptatum zzril delenit augue duis dolore te feugait nulla facilisi. Nam liber tempor cum soluta nobis eleifend option congue nihil imperdiet doming id quod mazim placerat facer possim assum. <a>Read More</a></p>
</section>
<section class="info abs" style="left:562px">
  <h4>News &amp; Events</h4>
  <p class="news"><span class="news-title">Bobis eleifend option congue nihil imperdiet</span>doming id quod mazim placerat facer possim assum. <a>Read More</a></p>
  <p class="news"><span class="news-title">Nnobis eleifend option congue nihil imperdiet</span>doming id quod mazim placerat facer possim assum. <a>Read More</a></p>
</section>

<footer class="site-footer abs">
  <div class="foot-col abs" style="left:126px;width:119px">
    <h5>Latest Posts</h5><div class="foot-line"></div>
    <ul><li>Lorem ipsum dotslor sicts adfmet</li><li>Nam non disam ersaddos dasssd</li><li>Vestibulum aliquet eros ut ipsum</li><li>Nullam blandit tristique lacuss is</li><li>Ut quis ante dui, eget scelerisque</li><li>Praesent tincidunt duid id sapien</li></ul>
  </div>
  <div class="foot-col abs" style="left:289px;width:105px">
    <h5>Site Links</h5><div class="foot-line"></div>
    <ul><li>Home (we start here)</li><li>About (get to know us better)</li><li>Services (all we do)</li><li>Galleries (see our work)</li><li>Blog (the news)</li><li>Contact (get in touch with us)</li></ul>
  </div>
  <div class="foot-col abs" style="left:435px;width:138px">
    <h5>Get a free qoute</h5><div class="foot-line"></div>
  </div>
  <div class="field abs" style="top:66px;height:16px">Name</div>
  <div class="field abs" style="top:88px;height:16px">Email</div>
  <div class="field abs" style="top:110px;height:30px">Message</div>
  <div class="submit abs">Submit</div>
  <div class="foot-col abs" style="left:600px;width:153px">
    <h5 style="padding-left:15px">We on maps</h5><div class="foot-line"></div>
  </div>
  <a class="cta abs" style="top:68px">
    <svg width="16" height="17" viewBox="0 0 16 17" aria-hidden="true"><rect x="1.5" y="2.5" width="13" height="13" fill="none" stroke="#fff" stroke-width="1.6"/><path d="M5 1v3M11 1v3M8 7v6M5 10l3 3 3-3" stroke="#fff" stroke-width="1.6" fill="none"/></svg>
    Order Form</a>
  <a class="cta abs" style="top:120px">
    <svg width="17" height="17" viewBox="0 0 17 17" aria-hidden="true"><circle cx="8.5" cy="8.5" r="6.5" fill="none" stroke="#fff" stroke-width="2.2"/><circle cx="8.5" cy="8.5" r="2.5" fill="#fff"/></svg>
    Digital Plan-room</a>
</footer>
<div class="footer-base abs">Copyright 2013 KPR. All Rights Reserved.</div>

</body>
</html>
```